Granite Ridge Response Business Card

Side 1: Granite Ridge Response Logo (logo without Maltese cross) with industrial rope rescue related theme. Our company services - TRAINING - Fire Training, Confined Space Rescue Training, Rope Rescue training, Hazmat Training, Incident Command, EMS, Pump Operations Training. Website - graniteridgeresponse.example.
Side 2: Granite Ridge Response Fire Department Logo (logo with Maltese cross) with Firefighter related theme. Company (division) services - FIELD SERVICES - Fire Department, Stand-by Rescue, Safety, EMS, Planning. "Supporting the Emergency Response Community Since 1967"

Add contact information wherever it makes since (Name, Email, Phone).
I would like it to represent the Granite Ridge Response Fire Department Logo as a division not as a separate entity without saying it, possibly by depicting it in the background of Side 2 instead of being a standalone picture like the logo on Side 1.

```html
<!DOCTYPE html>
<html lang="en">
<head>
<meta charset="utf-8">
<title>Granite Ridge Response Business Cards</title>
<link href="https://fonts.googleapis.com/css2?family=Montserrat:wght@400;600;700&family=Oswald:wght@500;600&display=swap" rel="stylesheet">
<style>
  :root {
    --bg: #3a3a3c;
    --card: #ffffff;
    --band: #262626;
    --ink: #1c1c1c;
    --red: #e8201e;
    --white: #ffffff;
    --photo-warm-1: #e9d9a6;
    --photo-warm-2: #f6efd9;
    --photo-cool-1: #c9ced6;
    --photo-cool-2: #eef0f3;
  }
  * { box-sizing: border-box; margin: 0; padding: 0; }
  html, body { width: 1200px; height: 1200px; overflow: hidden; }
  body {
    background: var(--bg);
    font-family: "Montserrat", Arial, sans-serif;
    position: relative;
  }
  .card {
    position: absolute;
    left: 80px;
    width: 1040px;
    height: 560px;
    background: var(--card);
    border-radius: 34px;
    overflow: hidden;
  }
  .card--field { top: 27px; }
  .card--training { top: 613px; }

  .photo { position: absolute; top: 0; bottom: 0; }
  .photo--firefighters {
    left: 0; width: 720px;
    background: radial-gradient(ellipse at 45% 55%, var(--photo-warm-1) 0%, var(--photo-warm-2) 55%, rgba(255,255,255,0) 80%);
  }
  .photo--rope {
    left: 330px; right: 0;
    background: radial-gradient(ellipse at 55% 55%, var(--photo-cool-1) 0%, var(--photo-cool-2) 55%, rgba(255,255,255,0) 85%);
  }

  .name-band {
    position: absolute;
    left: 0; top: 140px;
    width: 640px; height: 130px;
    background: var(--band);
    padding: 22px 0 0 110px;
    color: var(--white);
  }
  .name-band .full-name { font-weight: 700; font-size: 48px; line-height: 1; letter-spacing: 0.5px; }
  .name-band .position { font-weight: 400; font-size: 30px; margin-top: 8px; letter-spacing: 1px; }

  .brand {
    position: absolute;
    left: 660px; top: 120px; width: 340px;
    display: flex; align-items: center; gap: 14px;
  }
  .brand-dot { width: 22px; height: 22px; border-radius: 50%; background: var(--red); flex: none; }
  .brand-name {
    font-weight: 700; font-size: 34px; line-height: 1.1; letter-spacing: 1px;
    text-transform: uppercase;
  }
  .card--field .brand-name { color: var(--ink); }
  .card--training .brand-name { color: var(--red); }

  .contacts {
    position: absolute; left: 110px; top: 290px;
    list-style: none; color: var(--ink);
    font-size: 25px; line-height: 1.45;
  }
  .contacts li { display: flex; align-items: center; gap: 14px; }
  .contacts svg { width: 26px; height: 26px; flex: none; }

  .services {
    position: absolute; left: 110px; bottom: 36px; right: 40px;
    font-family: "Oswald", "Arial Narrow", sans-serif;
    font-weight: 500; font-size: 27px; line-height: 1.2;
    color: var(--ink); text-transform: uppercase;
  }
  .services-head { display: flex; align-items: baseline; }
  .services .group { color: var(--red); font-weight: 600; font-size: 30px; width: 450px; }
  .services-label { color: var(--red); font-weight: 600; font-size: 30px; }
  .services .sep { color: var(--red); }
</style>
</head>
<body>

<section class="card card--field">
  <div class="photo photo--firefighters" role="img" aria-label="Faded photo of two firefighters in turnout gear holding a hose"></div>
  <div class="name-band">
    <div class="full-name">FULL NAME</div>
    <div class="position">POSITION</div>
  </div>
  <div class="brand">
    <span class="brand-dot"></span>
    <span class="brand-name">Granite Ridge Response</span>
  </div>
  <ul class="contacts">
    <li><svg viewBox="0 0 24 24"><path fill="#e8201e" d="M6.6 10.8a15 15 0 0 0 6.6 6.6l2.2-2.2a1 1 0 0 1 1-.25 11.4 11.4 0 0 0 3.6.57 1 1 0 0 1 1 1V20a1 1 0 0 1-1 1A17 17 0 0 1 3 4a1 1 0 0 1 1-1h3.5a1 1 0 0 1 1 1 11.4 11.4 0 0 0 .57 3.6 1 1 0 0 1-.25 1z"/></svg>000 000 0000</li>
    <li><svg viewBox="0 0 24 24"><rect x="2" y="5" width="20" height="14" fill="#e8201e"/><path d="M2 5l10 8 10-8" fill="none" stroke="#fff" stroke-width="1.6"/></svg>info@graniteridgeresponse.example</li>
    <li><svg viewBox="0 0 24 24"><g fill="none" stroke="#e8201e" stroke-width="2"><circle cx="12" cy="12" r="9.5"/><ellipse cx="12" cy="12" rx="4" ry="9.5"/><path d="M2.5 12h19M4 7h16M4 17h16"/></g></svg>graniteridgeresponse.example</li>
  </ul>
  <div class="services">
    <div class="services-head"><div class="group">Field Services</div><div class="services-label">Services</div></div>
    <div>Fire Department <span class="sep">•</span> Stand-by Rescue <span class="sep">•</span> Safety <span class="sep">•</span> EMS <span class="sep">•</span> Planning</div>
    <div>"Supporting the Emergency Response Community Since 1967"</div>
  </div>
</section>

<section class="card card--training">
  <div class="photo photo--rope" role="img" aria-label="Faded photo of a rescuer suspended on ropes beside an industrial structure"></div>
  <div class="name-band">
    <div class="full-name">FULL NAME</div>
    <div class="position">POSITION</div>
  </div>
  <div class="brand">
    <span class="brand-dot"></span>
    <span class="brand-name">Granite Ridge Response</span>
  </div>
  <ul class="contacts">
    <li><svg viewBox="0 0 24 24"><path fill="#e8201e" d="M6.6 10.8a15 15 0 0 0 6.6 6.6l2.2-2.2a1 1 0 0 1 1-.25 11.4 11.4 0 0 0 3.6.57 1 1 0 0 1 1 1V20a1 1 0 0 1-1 1A17 17 0 0 1 3 4a1 1 0 0 1 1-1h3.5a1 1 0 0 1 1 1 11.4 11.4 0 0 0 .57 3.6 1 1 0 0 1-.25 1z"/></svg>000 000 0000</li>
    <li><svg viewBox="0 0 24 24"><rect x="2" y="5" width="20" height="14" fill="#e8201e"/><path d="M2 5l10 8 10-8" fill="none" stroke="#fff" stroke-width="1.6"/></svg>info@graniteridgeresponse.example</li>
    <li><svg viewBox="0 0 24 24"><g fill="none" stroke="#e8201e" stroke-width="2"><circle cx="12" cy="12" r="9.5"/><ellipse cx="12" cy="12" rx="4" ry="9.5"/><path d="M2.5 12h19M4 7h16M4 17h16"/></g></svg>graniteridgeresponse.example</li>
  </ul>
  <div class="services">
    <div class="services-head"><div class="group">Training</div><div class="services-label">Services</div></div>
    <div>Fire Training <span class="sep">•</span> Confined Space Rescue Training <span class="sep">•</span> Rope Rescue Training</div>
    <div>Hazmat Training <span class="sep">•</span> Incident Command <span class="sep">•</span> EMS <span class="sep">•</span> Pump Operations Training</div>
  </div>
</section>

</body>
</html>
```